6 Page Brochure for Car Dealers

1. We are an an accident management company in Sydney. Our website is wheelfix.com.au. We provide services for car dealers.

2. We need a 6 page brochure which we can leave with car dealers after we visit them. An example of what we are after is at :
http://www.layoutnest.com/wp-content/uploads/2014/02/Zo-Trend-Auto-Shine-brochure-1.jpg
http://www.layoutnest.com/wp-content/uploads/2014/02/Zo-Trend-Auto-Shine-brochure-3.jpg

3. The layout of the brochure is proposed as follows:

Page 1 - Title page with our logo, visual representation of a happy car dealer, and call to action such as "Try accident management to supercharge profits"

Page 2 - Qualifier page - compares a successful dealership vs an unsuccessful dealership...need a comparison layout similar to this:

https://img-store-bx3.snapboardia.com/736x/a1/42/93/a1429375bd2e6c1047fa3b815ec2d7a9.jpg

Page 3 - Benefits page which shows the customer's journey
Something similar to:

https://www.ridgeservers.com/wp-content/uploads/2015/03/rs-benefits-pdf.png/

Page 4: How to get started page which identifies a four step process: signing agreement, us providing training, reporting accidents using an online portal, collecting payment from us.

Page 5: Testimonials page from other dealerships
Visual logos of our different smash repairer partners

Page 6: Team and contact page with group shot of our whole company, map of where our office is located and office contact details.

Please let us know if you may design something for us.

Target Market(s)

Car dealers

Industry/Entity Type

Car Dealer

Font styles to use
Sans Serif

Colors
f04a50
ec1f27
f59296
fbd4d5

Requirements
Must have
• Please project description
Nice to have

```html
<!DOCTYPE html>
<html lang="en">
<head>
<meta charset="utf-8">
<title>WheelFix Dealer Brochure</title>
<link href="https://fonts.googleapis.com/css2?family=Montserrat:wght@400;600;700;800&family=Open+Sans:wght@400;600&display=swap" rel="stylesheet">
<style>
:root{
  --red:#ec1f27;
  --red-dark:#a9141a;
  --coral:#f04a50;
  --pink:#f59296;
  --blush:#fbd4d5;
  --grey-bg:#8e8e8e;
  --paper:#ffffff;
  --light:#ececec;
  --mid:#c9c9c9;
  --charcoal:#2a2a2a;
  --ink:#3a3a3a;
}
*{box-sizing:border-box;margin:0;padding:0}
html,body{width:1200px;height:2544px;overflow:hidden}
body{background:var(--grey-bg);position:relative;font-family:"Open Sans",Arial,sans-serif;color:var(--ink)}
.page{position:absolute;left:80px;width:1040px;height:560px;overflow:hidden;background:var(--paper);box-shadow:0 10px 30px rgba(0,0,0,.35)}
.cover{top:60px}
.spread-qualifier{top:680px}
.spread-start{top:1300px}
.back-cover{top:1920px}
.abs{position:absolute}
.shape{position:absolute;inset:0;width:100%;height:100%}
.placeholder{position:absolute}
.brand{position:absolute;display:flex;align-items:center;gap:8px;font-family:"Montserrat",Arial,sans-serif;font-weight:800;color:var(--red);letter-spacing:.5px}
.brand .dot{width:14px;height:14px;background:var(--red);border-radius:50%}
.head{font-family:"Montserrat",Arial,sans-serif;font-weight:800;text-transform:uppercase}
.small{font-size:9px;line-height:1.45}
.fold{position:absolute;left:520px;top:0;width:2px;height:100%;background:rgba(0,0,0,.12)}

/* cover */
.cover-photo{left:0;top:0;width:1040px;height:330px;background:linear-gradient(135deg,#d9dde2,#f3f3f3 45%,#b9bec4)}
.cover-car{left:40px;top:255px;width:330px;height:110px;background:linear-gradient(180deg,#e7e7e7,#8d8f93);border-radius:40px 60px 10px 10px}
.cover-headline{left:40px;top:385px;color:#fff}
.cover-headline .line1{font-size:30px;font-weight:600;font-family:"Montserrat",Arial,sans-serif;letter-spacing:.5px}
.cover-headline .line2{font-size:42px;line-height:1.05}
.cover-sub{left:40px;top:490px;background:var(--charcoal);color:#fff;font-size:11px;letter-spacing:3px;padding:6px 14px;text-transform:uppercase}
.cover .brand{right:50px;bottom:55px;font-size:40px}
.cover .tagline{position:absolute;right:50px;bottom:38px;font-size:11px;color:var(--red);font-style:italic}

/* qualifier spread */
.qual-title{left:30px;top:30px;font-size:13px;color:var(--charcoal);letter-spacing:1px}
.figure{background:linear-gradient(180deg,var(--coral),var(--red-dark));border-radius:6px}
.fig-unsuccess{left:330px;top:50px;width:90px;height:110px}
.fig-success{left:50px;top:325px;width:90px;height:115px;background:linear-gradient(180deg,#555,#1e1e1e)}
.label-unsuccess{left:300px;top:172px;font-size:14px;color:#fff;line-height:1.1}
.label-success{left:40px;top:456px;width:190px;font-size:15px;color:var(--charcoal);line-height:1.1}
.icon-row{display:flex;align-items:center;gap:6px;font-size:8px;color:var(--charcoal);width:140px}
.icon-row .ring{flex:none;width:24px;height:24px;border:2px solid var(--red);border-radius:50%;background:#fff}
.help-band{left:560px;top:40px;width:300px;background:var(--red);color:#fff;font-size:14px;padding:6px 12px}
.benefit-band{left:560px;top:270px;width:300px;background:var(--red);color:#fff;font-size:14px;padding:6px 12px}
.help-text{left:560px;top:80px;width:300px;color:var(--ink)}
.benefit-text{left:560px;top:310px;width:300px;color:var(--ink)}
.photo-col{left:880px;width:140px;height:120px;background:linear-gradient(135deg,#6b6f75,#c9ccd0)}
.spread-qualifier .brand{left:320px;top:236px;font-size:22px;color:#fff}

/* get started spread */
.start-title{left:30px;top:110px;font-size:22px;color:var(--charcoal)}
.start-title span{color:var(--red)}
.spread-start .brand{left:150px;top:40px;font-size:30px}
.step{position:absolute;width:86px;height:54px;color:#fff;font-family:"Montserrat",Arial,sans-serif;font-weight:700;font-size:10px;display:flex;align-items:center;justify-content:center;text-align:center;padding:0 16px 0 8px}
.step svg{position:absolute;inset:0;z-index:-1}
.steps{position:absolute;left:30px;top:190px;width:300px;height:300px;z-index:0}
.step-label{position:absolute;font-size:8px;width:110px;color:var(--ink)}
.presenter{left:330px;top:150px;width:170px;height:370px;background:linear-gradient(180deg,#cfd3d8,#8f949a)}
.testi-title{left:560px;top:35px;font-size:22px;color:var(--charcoal)}
.testi{position:absolute;left:560px;width:300px;display:flex;gap:12px}
.testi .avatar{flex:none;width:44px;height:44px;border-radius:50%;background:linear-gradient(135deg,#b8a89b,#6e625a);border:2px solid var(--red)}
.testi .name{font-family:"Montserrat",Arial,sans-serif;font-weight:700;font-size:10px;color:var(--red)}
.partners{position:absolute;left:560px;top:445px;display:flex;gap:14px}
.partners div{width:64px;height:30px;background:var(--mid);border-radius:4px}
.url-band{position:absolute;left:520px;bottom:0;width:520px;height:40px;background:var(--charcoal);color:#fff;font-size:12px;letter-spacing:2px;display:flex;align-items:center;justify-content:center}

/* back cover */
.team-photo{left:300px;top:0;width:740px;height:330px;background:linear-gradient(135deg,#7a1114,#c31a21 50%,#e75c60)}
.map{left:0;top:230px;width:340px;height:330px;background:linear-gradient(135deg,#f1f1f1,#dcdcdc)}
.contact{left:30px;top:340px;width:260px}
.contact h3{font-family:"Montserrat",Arial,sans-serif;font-weight:700;font-size:16px;color:var(--red);margin-bottom:10px}
.contact-row{display:flex;align-items:center;gap:8px;font-size:10px;margin-bottom:8px;color:var(--charcoal)}
.contact-row svg{flex:none}
.back-cover .brand{right:50px;bottom:55px;font-size:40px}
.back-cover .tagline{position:absolute;right:50px;bottom:38px;font-size:11px;color:var(--red);font-style:italic}
.addr{left:30px;top:250px;width:220px;font-size:9px;color:var(--charcoal);line-height:1.5}
</style>
</head>
<body>

<!-- Front cover -->
<section class="page cover">
  <div class="placeholder cover-photo" role="img" aria-label="Photo of a smiling car dealer handing keys to a happy family in a showroom"></div>
  <svg class="shape" viewBox="0 0 1040 560" preserveAspectRatio="none" aria-hidden="true">
    <polygon points="0,250 1040,150 1040,560 0,560" fill="var(--red)"/>
    <polygon points="0,250 1040,150 1040,175 0,285" fill="var(--red-dark)"/>
    <polygon points="620,560 1040,330 1040,560" fill="var(--paper)"/>
    <polygon points="590,560 1040,310 1040,330 620,560" fill="var(--charcoal)"/>
  </svg>
  <div class="placeholder cover-car" role="img" aria-label="Silver sedan car"></div>
  <div class="abs cover-headline">
    <div class="line1">TRY ACCIDENT MANAGEMENT TO</div>
    <div class="head line2">SUPERCHARGE PROFITS</div>
  </div>
  <div class="abs cover-sub">Smart claims for smart dealers</div>
  <div class="brand"><span class="dot"></span>WheelFix</div>
  <div class="tagline">claims made simple</div>
</section>

<!-- Pages 2–3 -->
<section class="page spread-qualifier">
  <svg class="shape" viewBox="0 0 1040 560" preserveAspectRatio="none" aria-hidden="true">
    <rect x="0" y="0" width="520" height="560" fill="var(--light)"/>
    <polygon points="170,0 520,0 520,290 260,290" fill="var(--red)"/>
    <polygon points="260,290 520,290 520,306 248,306" fill="var(--red-dark)"/>
    <polygon points="860,0 1040,0 1040,40 860,70" fill="var(--red)"/>
    <polygon points="520,520 1040,470 1040,560 520,560" fill="var(--red)"/>
  </svg>
  <div class="abs head qual-title">Qualifier</div>
  <div class="placeholder figure fig-unsuccess" role="img" aria-label="Illustration of a frustrated dealer at a desk"></div>
  <div class="abs head label-unsuccess">Unsuccessful<br>Dealership</div>
  <div class="placeholder figure fig-success" role="img" aria-label="Illustration of a confident dealer in a suit"></div>
  <div class="abs head label-success">Successful<br>Dealership</div>
  <div class="abs icon-row" style="left:40px;top:80px"><span class="ring"></span>Lost repair work</div>
  <div class="abs icon-row" style="left:40px;top:125px"><span class="ring"></span>Unhappy customers</div>
  <div class="abs icon-row" style="left:40px;top:170px"><span class="ring"></span>Slow claims</div>
  <div class="abs icon-row" style="left:40px;top:215px"><span class="ring"></span>No extra income</div>
  <div class="abs icon-row" style="left:260px;top:340px"><span class="ring"></span>Loyal customers</div>
  <div class="abs icon-row" style="left:260px;top:385px"><span class="ring"></span>Fast repairs</div>
  <div class="abs icon-row" style="left:260px;top:430px"><span class="ring"></span>New referral fees</div>
  <div class="abs icon-row" style="left:260px;top:475px"><span class="ring"></span>Higher profits</div>
  <div class="brand"><span class="dot"></span>WheelFix</div>
  <div class="fold"></div>
  <div class="abs head help-band">How we help motor dealers</div>
  <div class="abs small help-text">When a customer has an accident, we handle the whole claim for them. We arrange a tow, a courtesy car and a trusted repairer, and we keep the customer informed at every step. Your customer stays with you, their car is fixed fast, and your service team gets the credit for a smooth result.</div>
  <div class="abs head benefit-band">Benefits for motor dealers</div>
  <div class="abs small benefit-text">Earn a fee on every claim you refer. Keep customers loyal to your dealership. Save staff time with our simple online portal. Get paid quickly and reliably every month.</div>
  <div class="placeholder photo-col" style="top:80px" role="img" aria-label="Photo of a damaged car at a repair shop"></div>
  <div class="placeholder photo-col" style="top:210px" role="img" aria-label="Photo of a mechanic at work"></div>
  <div class="placeholder photo-col" style="top:340px" role="img" aria-label="Photo of a customer receiving car keys"></div>
</section>

<!-- Pages 4–5 -->
<section class="page spread-start">
  <svg class="shape" viewBox="0 0 1040 560" preserveAspectRatio="none" aria-hidden="true">
    <polygon points="340,0 520,0 520,200" fill="var(--red)"/>
    <polygon points="880,0 1040,0 1040,260" fill="var(--red)"/>
    <polygon points="840,0 880,0 1040,260 1040,300" fill="var(--charcoal)"/>
  </svg>
  <div class="brand"><span class="dot"></span>WheelFix</div>
  <div class="abs head start-title">How to <span>get started</span></div>
  <div class="steps">
    <div class="step" style="left:0;top:0"><svg viewBox="0 0 86 54" aria-hidden="true"><polygon points="0,0 70,0 86,27 70,54 0,54" fill="var(--red)"/></svg>01</div>
    <div class="step-label" style="left:96px;top:14px">Sign our simple dealer agreement</div>
    <div class="step" style="left:0;top:75px"><svg viewBox="0 0 86 54" aria-hidden="true"><polygon points="0,0 70,0 86,27 70,54 0,54" fill="var(--coral)"/></svg>02</div>
    <div class="step-label" style="left:96px;top:89px">We provide training for your team</div>
    <div class="step" style="left:0;top:150px"><svg viewBox="0 0 86 54" aria-hidden="true"><polygon points="0,0 70,0 86,27 70,54 0,54" fill="var(--red)"/></svg>03</div>
    <div class="step-label" style="left:96px;top:164px">Report accidents on our online portal</div>
    <div class="step" style="left:0;top:225px"><svg viewBox="0 0 86 54" aria-hidden="true"><polygon points="0,0 70,0 86,27 70,54 0,54" fill="var(--red-dark)"/></svg>04</div>
    <div class="step-label" style="left:96px;top:239px">Collect your payment from us</div>
  </div>
  <div class="placeholder presenter" role="img" aria-label="Photo of a smiling businesswoman holding a clipboard"></div>
  <div class="fold"></div>
  <div class="abs head testi-title">Testimonial</div>
  <div class="testi" style="top:80px"><div class="avatar" role="img" aria-label="Portrait of dealership manager"></div><div><div class="name">Harbour Motors</div><p class="small">Claims are handled fast and our customers come back happy every time.</p></div></div>
  <div class="testi" style="top:170px"><div class="avatar" role="img" aria-label="Portrait of dealership manager"></div><div><div class="name">Parkside Auto</div><p class="small">An easy extra income stream with almost no work for our staff.</p></div></div>
  <div class="testi" style="top:260px"><div class="avatar" role="img" aria-label="Portrait of dealership manager"></div><div><div class="name">Westgate Cars</div><p class="small">The portal is simple and payments always arrive on time.</p></div></div>
  <div class="testi" style="top:350px"><div class="avatar" role="img" aria-label="Portrait of dealership manager"></div><div><div class="name">Bayview Motor Group</div><p class="small">Our service department has never been busier. Highly recommended.</p></div></div>
  <div class="partners" aria-label="Repair partner badges"><div></div><div></div><div></div><div></div></div>
  <div class="url-band">www.wheelfix.com.au</div>
</section>

<!-- Back cover -->
<section class="page back-cover">
  <div class="placeholder team-photo" role="img" aria-label="Group photo of the whole company team on a red background"></div>
  <svg class="shape" viewBox="0 0 1040 560" preserveAspectRatio="none" aria-hidden="true">
    <polygon points="200,0 300,0 560,560 460,560" fill="var(--charcoal)"/>
    <polygon points="300,0 320,0 580,560 560,560" fill="#5a5a5a"/>
    <polygon points="580,560 1040,330 1040,560" fill="var(--paper)"/>
  </svg>
  <div class="placeholder map" role="img" aria-label="Street map showing the office location in Sydney" style="clip-path:polygon(0 0,40% 0,100% 100%,0 100%)"></div>
  <div class="abs addr">Unit 12, 45 Harbour Road<br>Sydney NSW 2000</div>
  <div class="abs contact">
    <h3>Contact us</h3>
    <div class="contact-row"><svg width="14" height="14" viewBox="0 0 24 24" aria-hidden="true"><path d="M12 2a7 7 0 0 0-7 7c0 5 7 13 7 13s7-8 7-13a7 7 0 0 0-7-7zm0 9.5a2.5 2.5 0 1 1 0-5 2.5 2.5 0 0 1 0 5z" fill="var(--red)"/></svg>Unit 12, 45 Harbour Road, Sydney NSW 2000</div>
    <div class="contact-row"><svg width="14" height="14" viewBox="0 0 24 24" aria-hidden="true"><path d="M6.6 10.8a15 15 0 0 0 6.6 6.6l2.2-2.2a1 1 0 0 1 1-.25 11.4 11.4 0 0 0 3.6.57 1 1 0 0 1 1 1V20a1 1 0 0 1-1 1A17 17 0 0 1 3 4a1 1 0 0 1 1-1h3.5a1 1 0 0 1 1 1c0 1.25.2 2.45.57 3.570a1 1 0 0 1-.25 1z" fill="var(--red)"/></svg>(02) 5550 1234</div>
    <div class="contact-row"><svg width="14" height="14" viewBox="0 0 24 24" aria-hidden="true"><rect x="3" y="3" width="18" height="18" rx="2" fill="var(--red)"/></svg>(02) 5550 1235</div>
    <div class="contact-row"><svg width="14" height="14" viewBox="0 0 24 24" aria-hidden="true"><path d="M3 5h18v14H3z" fill="var(--red)"/><path d="M3 5l9 7 9-7" stroke="#fff" stroke-width="1.6" fill="none"/></svg>info@wheelfix.com.au</div>
  </div>
  <div class="brand"><span class="dot"></span>WheelFix</div>
  <div class="tagline">claims made simple</div>
</section>

</body>
</html>
```